Electrical Engineering Business Card Design

I need a business card design for an engineering consulting company based in Orlando, FL. I have had a logo created which the files are attached. We work primarily in the theme park and entertainment market sector but do projects in all market sectors. We have been serving Central Florida since 1994 and continue to strive to serve our clients and provide outstanding designs.
Theme Park

```html
<!DOCTYPE html>
<html lang="en">
<head>
<meta charset="utf-8">
<title>Voltaris Engineering – Business Card</title>
<link rel="stylesheet" href="https://fonts.googleapis.com/css2?family=Mulish:wght@300;700&display=swap">
<style>
  :root {
    --forest: #006633;
    --lime: #8dc63f;
    --paper: #ffffff;
    --edge: #0a3d22;
    --shadow: rgba(0, 0, 0, 0.35);
  }
  * { box-sizing: border-box; margin: 0; padding: 0; }
  html, body {
    width: 1200px; height: 1200px; overflow: hidden;
    background: var(--paper);
    font-family: "Mulish", sans-serif;
  }
  .canvas { position: relative; width: 1200px; height: 1200px; }
  .card {
    position: absolute; left: 306px; width: 544px; height: 303px;
    background: var(--forest);
    border: 1px solid var(--edge);
    box-shadow: 6px 6px 6px var(--shadow);
    overflow: hidden;
  }
  .card--front { top: 196px; }
  .card--back { top: 631px; }
  .brand-band {
    position: absolute; left: 0; width: 100%;
    background: var(--lime);
    display: flex; align-items: center; justify-content: center;
  }
  .card--front .brand-band { top: 23px; height: 81px; }
  .card--back .brand-band { top: 105px; height: 86px; }
  .brand-band__name {
    margin-left: -16px;
    font-family: "Mulish", sans-serif; font-weight: 700; font-size: 26px;
    letter-spacing: 1px; color: var(--forest);
  }
  .company-name {
    position: absolute; top: 147px; left: 0; width: 100%;
    text-align: center; color: var(--lime);
    font-weight: 700; font-size: 30px; letter-spacing: 0.5px;
  }
  .contact {
    position: absolute; top: 224px; left: 0; width: 100%; height: 60px;
    color: var(--lime); font-size: 15px; line-height: 20px; font-weight: 300;
  }
  .contact__address {
    position: absolute; right: 294px; top: 0; text-align: right; white-space: nowrap;
  }
  .contact__divider {
    position: absolute; left: 279px; top: 2px; width: 2px; height: 50px;
    background: var(--lime);
  }
  .contact__lines { position: absolute; left: 309px; top: 0; white-space: nowrap; }
  .contact__label { display: inline-block; width: 54px; }
</style>
</head>
<body>
<main class="canvas">
  <section class="card card--front" aria-label="Business card front">
    <div class="brand-band"><span class="brand-band__name">VOLTARIS</span></div>
    <h1 class="company-name">Voltaris Engineering, PA</h1>
    <div class="contact">
      <p class="contact__address">PO Box 481207<br>Orlando, FL 32819<br>email: dan.reyes@voltaris-eng.com</p>
      <span class="contact__divider"></span>
      <p class="contact__lines">
        <span class="contact__label">phone:</span>407-555-0142<br>
        <span class="contact__label">fax:</span>407-555-0187
      </p>
    </div>
  </section>

  <section class="card card--back" aria-label="Business card back">
    <div class="brand-band"><span class="brand-band__name">VOLTARIS</span></div>
  </section>
</main>
</body>
</html>
```